Notary Signing Agent Need Business card Design

Need a Business card design for my new company. RT Velo-Brisk LLC
Mobile Notary Signing Agent. I go to the customer for closing of Mortgage's Documents . possible signs of honesty, integrity and confidentiality.

Work with Title company to Notary Mortgage closing.

My Target Market is Title companies. Banks and Financial Institution.

Color Blue to Black Professional ) if needed some Green Little Red

And possible a company logo.

Mobile ( travel to clients ) Integrity, Honest Trustworthy. A show of Professional services.

Would like company name and my name on card

Use both sides and front with business name and my name. phone numbers.

Target Market(s)

Title company, Banks mortgage company

Industry/Entity Type

Travel

Contact Information for Business Card

Notary, Certified signing agent, Mobile

Colors
0455a3

Requirements
Must have
• Name of company , owners name phone number,
Nice to have
• blue and black color like a professional look but not limit to these only.
• a stand out from other cards .

```html
<!DOCTYPE html>
<html lang="en">
<head>
<meta charset="utf-8">
<title>RT Velo-Brisk LLC – Business Card</title>
<link rel="stylesheet" href="https://fonts.googleapis.com/css2?family=Questrial&display=swap">
<style>
  :root {
    --page-bg: #e3e4e5;
    --card-black: #030303;
    --brand-blue: #0455a3;
    --ink-dark: #111111;
    --text-light: #dcdcdc;
    --text-grey: #bdbdbd;
  }
  * { margin: 0; padding: 0; box-sizing: border-box; }
  html, body {
    width: 1200px;
    height: 799px;
    overflow: hidden;
  }
  body {
    background: var(--page-bg);
    font-family: "Questrial", "Century Gothic", sans-serif;
    position: relative;
  }
  .brand-lockup {
    position: absolute;
    top: 100px;
    left: 840px;
    width: 300px;
    display: flex;
    align-items: center;
    justify-content: center;
    gap: 14px;
  }
  .brand-lockup .brand-mark {
    width: 26px;
    height: 26px;
    flex: none;
    background: var(--brand-blue);
  }
  .brand-lockup .brand-name {
    color: var(--ink-dark);
    font-size: 30px;
    letter-spacing: 0.02em;
    white-space: nowrap;
  }
  .card {
    position: absolute;
    top: 240px;
    width: 520px;
    height: 300px;
    background: var(--card-black);
    box-shadow: 0 1px 2px rgba(0,0,0,0.25);
  }
  .card-front { left: 50px; }
  .card-back { left: 630px; }
  .card-front .front-lockup {
    position: absolute;
    inset: 0;
    display: flex;
    align-items: center;
    justify-content: center;
    gap: 14px;
  }
  .card-front .brand-mark {
    width: 28px;
    height: 28px;
    flex: none;
    background: var(--brand-blue);
  }
  .card-front .brand-name {
    color: var(--brand-blue);
    font-size: 34px;
    letter-spacing: 0.02em;
    white-space: nowrap;
  }
  .card-back .company-name {
    position: absolute;
    top: 50px;
    width: 100%;
    text-align: center;
    color: var(--brand-blue);
    font-size: 17px;
    letter-spacing: 0.02em;
  }
  .card-back .holder-name {
    position: absolute;
    top: 118px;
    width: 100%;
    text-align: center;
    color: var(--text-light);
    font-size: 23px;
    letter-spacing: 0.02em;
  }
  .card-back .contact-lines {
    position: absolute;
    top: 162px;
    width: 100%;
    text-align: center;
    color: var(--text-grey);
    font-size: 15px;
    line-height: 1.3;
    list-style: none;
  }
</style>
</head>
<body>
  <div class="brand-lockup">
    <span class="brand-mark"></span>
    <span class="brand-name">RT Velo-Brisk LLC</span>
  </div>

  <section class="card card-front" aria-label="Card front">
    <div class="front-lockup">
      <span class="brand-mark"></span>
      <span class="brand-name">RT Velo-Brisk LLC</span>
    </div>
  </section>

  <section class="card card-back" aria-label="Card back">
    <p class="company-name">RT Velo-Brisk LLC.</p>
    <p class="holder-name">Daniel R Hale</p>
    <ul class="contact-lines">
      <li>C: 555-014-2671</li>
      <li>F: 555-017-3308</li>
    </ul>
  </section>
</body>
</html>
```